Virtual Reality company needs business card design

We would like a business card that is simple and memorable. Vantelo is a global startup based in San Francisco and Singapore. We are a company with products and services for both the B2B and B2C audiences. We develop platforms with educational content, and allow people to interact with the content in a virtual environment setting. Our end user will be able to learn and 'see' the world's culture and history from the comfort of their home. The business card will primarily be used for B2B audience and not overly corporate in image, but requires a universal appeal - evoking sense of friendliness and innovation. Attached is our logo with two color options. We are open to single-sided or double-sided designs. EPS/AI files will be provided to winning designer at final design stage.

Other text that will be included in card: (Name), (Address), (Tel), (Email), (Website)

Include option of having TWO QR codes which are 0.5 inch x 0.5 inch each
Updates

Dear Designers,

Thank you for your submissions. We are currently in process of reviewing your designs and will make a decision in the next few days.

Regards,
Vantelo

Industry/Entity Type

Environment

Font styles to use
Serif
Sans Serif

Requirements
Must have
• Spacing for Name, Address, Tel, Email, Web address
Should not have
• Limit the number of colors utilised.

```html
<!DOCTYPE html>
<html lang="en">
<head>
<meta charset="utf-8">
<title>Vantelo Business Card</title>
<link href="https://fonts.googleapis.com/css2?family=Source+Sans+3:wght@400;600&display=swap" rel="stylesheet">
<style>
:root{
  --bg:#efe9e1;
  --card-white:#ffffff;
  --card-black:#000000;
  --brand-blue:#3399d6;
  --brand-teal:#62c2d2;
  --ink:#3d3d3d;
  --rule:#b8b8b8;
}
*{margin:0;padding:0;box-sizing:border-box}
html,body{width:1200px;height:1185px;overflow:hidden;background:var(--bg)}
body{position:relative;font-family:"Source Sans 3",sans-serif}
.card{position:absolute;overflow:hidden}
.card-front{left:229px;top:45px;width:933px;height:538px;background:var(--card-white);box-shadow:0 2px 6px rgba(0,0,0,.25)}
.card-back{left:30px;top:615px;width:935px;height:532px;background:var(--card-black);box-shadow:0 2px 6px rgba(0,0,0,.3)}
.front-wordmark{position:absolute;left:0;width:100%;top:38px;text-align:center;font-size:150px;font-weight:400;color:var(--brand-blue);line-height:1;letter-spacing:2px}
.identity{position:absolute;right:503px;top:252px;text-align:right;color:var(--ink);font-size:24px;line-height:36px}
.identity .person-name{color:var(--brand-blue);font-weight:600;font-size:30px;line-height:36px}
.divider{position:absolute;left:447px;top:250px;width:2px;height:150px;background:var(--rule)}
.contacts{position:absolute;left:464px;top:252px;list-style:none;color:var(--ink);font-size:24px;line-height:34.5px}
.contacts li{display:flex;align-items:center;gap:8px}
.contacts svg{width:20px;height:20px;flex:none}
.wave{position:absolute;left:0;bottom:0;width:933px;height:140px}
.back-wordmark{position:absolute;left:0;width:100%;top:150px;text-align:center;font-size:150px;font-weight:400;color:var(--brand-blue);line-height:1}
.back-url{position:absolute;left:0;width:100%;top:440px;text-align:center;color:#fff;font-size:31px;letter-spacing:2.5px}
</style>
</head>
<body>
<section class="card card-front">
  <div class="front-wordmark">Vantelo</div>
  <div class="identity">
    <div class="person-name">Your Name</div>
    <div>Title</div>
    <div>Street Name, City Name</div>
    <div>Zip Code-00000</div>
  </div>
  <div class="divider"></div>
  <ul class="contacts">
    <li><svg viewBox="0 0 20 20"><circle cx="10" cy="10" r="8" fill="none" stroke="var(--brand-blue)" stroke-width="2"/><path d="M7 6c0 5 2 8 6 8l1-2-2-1-1 1c-1-1-2-2-2-4l1-1-1-2z" fill="var(--brand-blue)"/></svg>012-555-0147</li>
    <li><svg viewBox="0 0 20 20"><rect x="5" y="2" width="10" height="16" rx="2" fill="var(--brand-blue)"/><rect x="7" y="4" width="6" height="7" fill="#fff"/></svg>012-555-0147</li>
    <li><svg viewBox="0 0 20 20"><rect x="2" y="5" width="16" height="11" rx="1.5" fill="var(--brand-blue)"/><path d="M2.5 6l7.5 6 7.5-6" fill="none" stroke="#fff" stroke-width="1.5"/></svg>hello@vantelo.com</li>
    <li><svg viewBox="0 0 20 20" fill="none" stroke="var(--brand-blue)" stroke-width="1.6"><circle cx="10" cy="10" r="8"/><ellipse cx="10" cy="10" rx="3.5" ry="8"/><path d="M2 10h16M3.5 6h13M3.5 14h13"/></svg>www.vantelo-vr.com</li>
  </ul>
  <svg class="wave" viewBox="0 0 933 140" preserveAspectRatio="none" aria-hidden="true">
    <path d="M0 0C60 20 110 60 230 68C420 80 620 40 760 50C840 56 900 80 933 95V140H0Z" fill="var(--brand-teal)"/>
    <path d="M0 62C90 100 200 108 330 100C520 88 700 64 933 105V140H0Z" fill="#fff"/>
    <path d="M0 70C90 108 200 116 330 108C520 96 700 72 933 112V140H0Z" fill="var(--brand-blue)"/>
  </svg>
</section>
<section class="card card-back">
  <div class="back-wordmark">Vantelo</div>
  <div class="back-url">www.vantelo-vr.com</div>
</section>
</body>
</html>
```